Ferncrest Dental, LLC business card project

Business card to be designed with current logo.
Dental office- please keep design of card that looks clean and professional.
Please include the following info:
Ferncrest Dental, LLC
Dr. Lorna Pettigrew
2871 Marlowe Street
Bethlehem, PA 18093
610-555-0193
ferncrestdental.office@examplemail.test
Hello everyone-
Reason: Just got back from overseas- will look at all designs and provide feedback. Thank you!
Reason: Polling my friends for the final selection-
thank you to all those that participated- so many talented designers!

```html
<!DOCTYPE html>
<html lang="en">
<head>
<meta charset="utf-8">
<title>Ferncrest Dental — Business Card</title>
<link rel="stylesheet" href="https://fonts.googleapis.com/css2?family=Questrial&display=swap">
<style>
  :root {
    --page-bg: #ffffff;
    --card-line: #b8b8b8;
    --brand-green: #b3d335;
    --deep-green: #5e9f2e;
    --ink: #1e1e1e;
    --white: #ffffff;
    --name-panel: rgba(255, 255, 255, 0.14);
  }
  * { margin: 0; padding: 0; box-sizing: border-box; }
  html, body {
    width: 1200px; height: 900px; overflow: hidden;
    background: var(--page-bg);
    font-family: "Questrial", "Century Gothic", sans-serif;
  }
  .canvas { position: relative; width: 1200px; height: 900px; }

  .card { position: absolute; top: 297px; width: 470px; height: 308px; }
  .card-front { left: 91px; }
  .card-back { left: 641px; }
  .card-shape { position: absolute; inset: 0; width: 470px; height: 308px; }

  .front-brand {
    position: absolute; left: 31px; top: 44px;
    display: flex; align-items: center; gap: 10px;
  }
  .brand-dot { width: 12px; height: 12px; border-radius: 50%; background: var(--brand-green); }
  .brand-name { font-size: 27px; color: var(--deep-green); letter-spacing: -0.3px; }

  .practice {
    position: absolute; left: 26px; top: 178px;
    color: var(--deep-green); font-size: 14.5px; line-height: 18px;
  }
  .contact {
    position: absolute; left: 26px; top: 233px;
    list-style: none; color: var(--ink); font-size: 11px; line-height: 13.5px;
  }
  .contact li { display: flex; }
  .contact .label { width: 20px; }
  .contact .sep { width: 9px; }

  .back-name-panel {
    position: absolute; left: 121px; top: 122px;
    width: 259px; height: 64px;
    background: var(--name-panel);
    display: flex; align-items: center; justify-content: center;
  }
  .back-name { color: var(--white); font-size: 33px; letter-spacing: -0.5px; }
</style>
</head>
<body>
<main class="canvas">
  <section class="card card-front" aria-label="Card front">
    <svg class="card-shape" viewBox="0 0 470 308" aria-hidden="true">
      <path d="M0.5 0.5 H469.5 V58 H394 V248 H469.5 V307.5 H0.5 Z"
            fill="var(--white)" stroke="var(--card-line)" stroke-width="1"/>
    </svg>
    <div class="front-brand">
      <span class="brand-dot"></span>
      <span class="brand-name">Ferncrest Dental</span>
    </div>
    <div class="practice">
      <p>Ferncrest Dental, LLC</p>
      <p>Dr. Lorna Pettigrew</p>
    </div>
    <ul class="contact">
      <li><span class="label">A</span><span class="sep">:</span><span>2871 Marlowe Street, Bethlehem, PA 18093</span></li>
      <li><span class="label">M</span><span class="sep">:</span><span>610-555-0193</span></li>
      <li><span class="label">E</span><span class="sep">:</span><span>ferncrestdental.office@examplemail.test</span></li>
    </ul>
  </section>

  <section class="card card-back" aria-label="Card back">
    <svg class="card-shape" viewBox="0 0 470 308" aria-hidden="true">
      <path d="M0 0 H470 V308 H0 V248 H76 V58 H0 Z" fill="var(--brand-green)"/>
    </svg>
    <div class="back-name-panel">
      <span class="back-name">Ferncrest Dental</span>
    </div>
  </section>
</main>
</body>
</html>
```